Stationary and design update for my brand

I need new letterhead, a new business card, business envelope design, new keynote and powerpoint branded slides (16x9). I have logo samples in various styles and brand standards for fonts and colors.

Font styles to use
Sans Serif

```html
<!DOCTYPE html>
<html lang="en">
<head>
<meta charset="utf-8">
<title>Ridgeway Stationery and Slides</title>
<link href="https://fonts.googleapis.com/css2?family=Cinzel:wght@400&family=Arimo:wght@400;700&display=swap" rel="stylesheet">
<style>
:root{
  --orange:#ef8a1f;
  --orange-soft:rgba(239,138,31,.55);
  --peach:#fbeadb;
  --peach-clear:rgba(251,234,219,0);
  --paper:#ffffff;
  --ground:#e9e9ec;
  --charcoal:#4a4a4d;
  --ink:#2b2b2b;
  --rule:#c9c9c9;
  --grey-text:#555;
}
*{margin:0;padding:0;box-sizing:border-box}
html,body{width:1200px;height:445px;overflow:hidden;background:var(--ground)}
.canvas{position:relative;width:1200px;height:445px;font-family:"Arimo",Arial,sans-serif;color:var(--ink)}
.piece{position:absolute;background:var(--paper);box-shadow:0 1px 3px rgba(0,0,0,.18);overflow:hidden}
.brand{position:relative;z-index:2;font-family:"Cinzel",Georgia,serif;font-weight:400;letter-spacing:.02em;line-height:1;white-space:nowrap}
.brand.on-orange{color:#fff}
.brand.on-white{color:var(--orange)}
.contact-row{display:flex;align-items:center;gap:1.5px}
.icon{width:3px;height:3px;flex:none}
.scenery{position:absolute;z-index:1}
.piece > *:not(.scenery){z-index:2}

/* business cards */
.card{width:100px;height:57px;top:57px}
.card-front{left:110px;background:var(--orange)}
.card-front .scenery{left:0;right:0;bottom:0;height:34px;background:linear-gradient(160deg,var(--orange) 15%,#f7c28c 55%,#fff 85%)}
.card-front .brand{position:absolute;left:6px;top:7px;font-size:7px}
.card-front .details{position:absolute;left:6px;top:17px;color:#fff;font-size:2.5px;line-height:1.35}
.card-front .holder{position:absolute;right:7px;bottom:5px;font-size:2.8px;line-height:1.3}
.card-front .holder b{font-family:"Cinzel",Georgia,serif;font-weight:400;letter-spacing:.03em;color:var(--orange);display:block}
.card-back{left:218px}
.card-back .scenery{left:0;right:0;top:0;height:100%;background:linear-gradient(170deg,var(--orange) 30%,#f6b878 55%,#fff 80%)}
.card-back .brand{position:absolute;right:7px;top:15px;font-size:8px}

/* envelopes */
.envelope-window{left:108px;top:130px;width:213px;height:106px}
.envelope-window .scenery{right:0;bottom:0;width:150px;height:75px;background:radial-gradient(ellipse at 65% 85%,var(--peach) 0,var(--peach) 35%,var(--peach-clear) 72%)}
.envelope-window .brand{position:absolute;left:8px;top:16px;font-size:11px}
.envelope-window .address{position:absolute;left:9px;top:33px;font-size:3.6px;line-height:1.3}
.envelope-flap{left:112px;top:248px;width:213px;height:107px;background:#f3f3f3}
.flap{position:absolute;left:0;top:0;width:100%;height:27px;background:var(--orange);border-radius:0 0 6px 6px;display:flex;align-items:center;justify-content:center}
.flap .brand{font-size:8px}
.envelope-dark{left:41px;top:284px;width:214px;height:107px;background:#f1f1f1}
.envelope-dark .flap{background:var(--charcoal)}

/* letterhead */
.letterhead{left:349px;top:57px;width:216px;height:304px}
.letterhead .scenery{left:0;right:0;bottom:0;height:80px;background:linear-gradient(to top,var(--peach) 0,var(--peach) 35%,var(--peach-clear) 100%)}
.letterhead .brand{position:absolute;left:11px;top:25px;font-size:12px}
.letterhead .contact{position:absolute;right:14px;top:14px;font-size:3.4px;line-height:1.3}
.letterhead .contact .contact-row{margin-top:1px}

/* note pads */
.pad-orange-small{left:635px;top:55px;width:55px;height:104px;background:var(--orange)}
.pad-orange-small .brand{position:absolute;left:12px;top:13px;font-size:7px}
.pad-orange-small .details{position:absolute;left:5px;bottom:5px;color:#fff;font-size:2.4px;line-height:1.3}
.pad-white-small{left:669px;top:84px;width:55px;height:103px}
.pad-white-small .brand{position:absolute;left:0;right:0;top:18px;text-align:center;font-size:7.5px}
.pad-white-small .scenery{left:0;right:0;bottom:7px;height:16px;background:linear-gradient(to top,var(--orange),rgba(239,138,31,0))}
.pad-white-small .foot{position:absolute;left:0;right:0;bottom:0;height:8px;background:var(--orange);color:#fff;font-family:"Cinzel",Georgia,serif;font-size:2.6px;text-align:center;line-height:8px}
.pad-lined-small{left:732px;top:56px;width:54px;height:102px}
.pad-lined-small .brand{position:absolute;right:3px;top:4px;font-size:3.4px}
.lines{position:absolute;left:4px;right:4px;background:repeating-linear-gradient(to bottom,transparent 0,transparent 5px,var(--rule) 5px,var(--rule) 5.4px)}
.pad-lined-small .lines{top:10px;height:80px}
.pad-lined-small .scenery{left:0;right:0;bottom:8px;height:22px;background:linear-gradient(to top,var(--peach),var(--peach-clear))}
.pad-lined-small .url{position:absolute;bottom:3px;left:0;right:0;text-align:center;font-size:2.3px;color:var(--grey-text)}

.spiral{position:absolute;left:0;right:0;top:0;height:3px;background:repeating-linear-gradient(to right,#3a3a3a 0,#3a3a3a .8px,transparent .8px,transparent 1.8px)}
.notebook{width:93px;height:121px}
.notebook-orange{left:621px;top:196px;background:var(--orange)}
.notebook-orange .brand{position:absolute;left:25px;top:17px;font-size:11px}
.notebook-orange .details{position:absolute;left:5px;bottom:14px;color:#fff;font-size:2.6px;line-height:1.3}
.notebook-white{left:643px;top:232px}
.notebook-white .brand{position:absolute;left:0;right:0;top:19px;text-align:center;font-size:11px}
.notebook-white .scenery{left:0;right:0;bottom:14px;height:28px;background:linear-gradient(to top,var(--orange),rgba(239,138,31,0))}
.notebook-white .foot{position:absolute;left:0;right:0;bottom:0;height:14px;background:var(--orange);color:#fff;font-family:"Cinzel",Georgia,serif;font-size:5px;text-align:center;line-height:14px}
.notebook-lined{left:745px;top:232px}
.notebook-lined .brand{position:absolute;right:6px;top:8px;font-size:5px}
.notebook-lined .lines{top:17px;height:96px;left:7px;right:7px;background:repeating-linear-gradient(to bottom,transparent 0,transparent 6px,var(--rule) 6px,var(--rule) 6.4px)}
.notebook-lined .scenery{left:0;right:0;bottom:9px;height:28px;background:linear-gradient(to top,var(--peach),var(--peach-clear))}
.notebook-lined .url{position:absolute;bottom:3px;left:0;right:0;text-align:center;font-size:3.6px;color:var(--grey-text)}

/* slides */
.slide{width:137px;height:77px}
.slide.col-a{left:863px}
.slide.col-b{left:1015px}
.slide.row-1{top:55px}
.slide.row-2{top:146px}
.slide.row-3{top:238px}
.slide-title{background:var(--orange)}
.slide-title .scenery{right:0;bottom:0;width:90px;height:45px;background:radial-gradient(ellipse at 70% 100%,#fff 0,#fbd7b0 30%,rgba(239,138,31,0) 70%)}
.slide-title .brand{position:absolute;left:11px;top:14px;font-size:9px}
.slide-title .welcome{position:absolute;left:11px;top:34px;color:#fff;font-family:"Cinzel",Georgia,serif;font-size:5px;line-height:1.2}
.slide-head{position:absolute;left:8px;right:8px;top:4px;height:7px;border-bottom:.5px solid var(--rule)}
.slide-head .mark{position:absolute;left:0;bottom:1px;width:16px;height:1.2px;background:var(--orange)}
.slide-head .heading{position:absolute;right:0;top:0;font-family:"Cinzel",Georgia,serif;color:var(--orange);font-size:4.6px}
.slide-foot{position:absolute;left:8px;right:9px;bottom:5px;height:3px;background:var(--orange);color:#fff;font-size:2px;font-family:"Cinzel",Georgia,serif;padding-left:1px;line-height:3px}
.photo{position:absolute}
.slide-photo .photo{left:8px;top:14px;width:121px;height:34px;background:linear-gradient(100deg,#9aa3ab,#d9d6d0 55%,#c0a58c)}
.bullets{position:absolute;font-size:2.3px;line-height:1.3;color:#333;list-style:none}
.bullets li{position:relative;padding-left:3px;margin-bottom:1.4px}
.bullets li::before{content:"";position:absolute;left:0;top:.8px;width:1.2px;height:1.2px;background:var(--orange);border-radius:50%}
.slide-photo .bullets{left:9px;right:9px;top:51px}
.slide-team .intro{position:absolute;left:9px;right:9px;top:14px;font-size:2.3px;line-height:1.3;color:#333}
.team{position:absolute;left:12px;right:12px;top:24px;display:flex;justify-content:space-between}
.member{width:22px;font-size:2.2px;line-height:1.3;color:#333}
.member .portrait{width:18px;height:18px;border-radius:50%;background:#c9b9a8;border:1px solid #eee;margin-bottom:2px}
.member i{color:var(--orange);display:block}
.slide-list .bullets{left:9px;right:9px;top:17px;font-size:2.4px}
.slide-list .bullets li{margin-bottom:3.2px}
.slide-feature .lead{position:absolute;left:9px;width:56px;top:15px;font-family:Georgia,serif;font-style:italic;color:var(--orange);font-size:3px;line-height:1.3}
.slide-feature .copy{position:absolute;left:9px;width:56px;top:25px;font-size:2.3px;line-height:1.35;color:#333}
.slide-feature .copy p{margin-bottom:2px}
.slide-feature .photo{left:73px;top:14px;width:52px;height:53px;background:linear-gradient(160deg,#b9c6d3,#5e7387 60%,#36475a)}
.slide-thanks{background:var(--orange);color:#fff}
.slide-thanks .scenery{left:0;right:0;top:0;height:50px;background:radial-gradient(ellipse at 50% 40%,rgba(255,255,255,.22) 0,rgba(255,255,255,0) 65%)}
.slide-thanks .word{position:absolute;left:0;right:0;top:39px;text-align:center;font-family:"Cinzel",Georgia,serif;font-size:11px}
.slide-thanks .details{position:absolute;left:8px;bottom:6px;font-size:2.8px;line-height:1.3;font-family:Georgia,serif}
.slide-thanks .address{position:absolute;right:9px;bottom:6px;font-size:2.8px;text-align:right;font-family:Georgia,serif;line-height:1.3}
</style>
</head>
<body>
<main class="canvas">

  <section class="piece card card-front">
    <div class="scenery" role="img" aria-label="Mountain range illustration"></div>
    <div class="brand on-orange">RIDGEWAY</div>
    <div class="details">
      <div>218 Alder Row, Suite 12</div>
      <div>Fairhaven, NC 28100</div>
      <div class="contact-row" style="margin-top:1.5px"><svg class="icon" viewBox="0 0 10 10"><circle cx="5" cy="5" r="5" fill="#fff"/></svg>(555) 014-2290</div>
      <div class="contact-row"><svg class="icon" viewBox="0 0 10 10"><rect x="1" y="2" width="8" height="6" fill="#fff"/></svg>dana@ridgeway-co.com</div>
      <div class="contact-row"><svg class="icon" viewBox="0 0 10 10"><circle cx="5" cy="5" r="4" fill="none" stroke="#fff" stroke-width="1.5"/></svg>www.ridgeway-co.com</div>
    </div>
    <div class="holder"><b>DANA WHITLOCK</b>Chief of Staff</div>
  </section>

  <section class="piece card card-back">
    <div class="scenery" role="img" aria-label="Mountain range illustration"></div>
    <div class="brand on-orange">RIDGEWAY</div>
  </section>

  <section class="piece envelope-window">
    <div class="scenery" role="img" aria-label="Faint mountain range illustration"></div>
    <div class="brand on-white">RIDGEWAY</div>
    <div class="address">218 Alder Row, Suite 12<br>Fairhaven, NC 28100</div>
  </section>

  <section class="piece envelope-flap">
    <div class="flap"><span class="brand on-orange">RIDGEWAY</span></div>
  </section>

  <section class="piece envelope-dark">
    <div class="flap"><span class="brand on-white">RIDGEWAY</span></div>
  </section>

  <section class="piece letterhead">
    <div class="scenery" role="img" aria-label="Faint mountain range illustration"></div>
    <div class="brand on-white">RIDGEWAY</div>
    <div class="contact">
      <div>218 Alder Row, Suite 12</div>
      <div>Fairhaven, NC 28100</div>
      <div class="contact-row" style="margin-top:2px"><svg class="icon" viewBox="0 0 10 10"><circle cx="5" cy="5" r="5" fill="var(--orange)"/></svg>(555) 014-2290</div>
      <div class="contact-row"><svg class="icon" viewBox="0 0 10 10"><rect x="1" y="2" width="8" height="6" fill="var(--orange)"/></svg>dana@ridgeway-co.com</div>
      <div class="contact-row"><svg class="icon" viewBox="0 0 10 10"><circle cx="5" cy="5" r="4" fill="none" stroke="var(--orange)" stroke-width="1.5"/></svg>www.ridgeway-co.com</div>
    </div>
  </section>

  <section class="piece pad-orange-small">
    <div class="brand on-orange">RIDGEWAY</div>
    <div class="details">(555) 014-2290<br>dana@ridgeway-co.com<br>www.ridgeway-co.com<br>218 Alder Row, Suite 12<br>Fairhaven, NC 28100</div>
  </section>
  <section class="piece pad-white-small">
    <div class="brand on-white">RIDGEWAY</div>
    <div class="scenery" role="img" aria-label="Mountain range illustration"></div>
    <div class="foot">WWW.RIDGEWAY-CO.COM</div>
  </section>
  <section class="piece pad-lined-small">
    <div class="brand on-white">RIDGEWAY</div>
    <div class="lines"></div>
    <div class="scenery" role="img" aria-label="Faint mountain range illustration"></div>
    <div class="url">www.ridgeway-co.com</div>
  </section>

  <section class="piece notebook notebook-orange">
    <div class="spiral"></div>
    <div class="brand on-orange">RIDGEWAY</div>
    <div class="details">218 Alder<br>(555) 014</div>
  </section>
  <section class="piece notebook notebook-white">
    <div class="spiral"></div>
    <div class="brand on-white">RIDGEWAY</div>
    <div class="scenery" role="img" aria-label="Mountain range illustration"></div>
    <div class="foot">WWW.RIDGEWAY-CO.COM</div>
  </section>
  <section class="piece notebook notebook-lined">
    <div class="spiral"></div>
    <div class="brand on-white">RIDGEWAY</div>
    <div class="lines"></div>
    <div class="scenery" role="img" aria-label="Faint mountain range illustration"></div>
    <div class="url">www.ridgeway-co.com</div>
  </section>

  <section class="piece slide slide-title col-a row-1">
    <div class="scenery" role="img" aria-label="Mountain range illustration"></div>
    <div class="brand on-orange">RIDGEWAY</div>
    <div class="welcome">Welcome to Our<br>Presentation Name<br>Description</div>
  </section>

  <section class="piece slide slide-photo col-b row-1">
    <div class="slide-head"><span class="mark"></span><span class="heading">HEADING HERE</span></div>
    <div class="photo" role="img" aria-label="Photo of colleagues meeting around a tablet in a bright office"></div>
    <ul class="bullets">
      <li>Clear goals shape every session we plan together.</li>
      <li>Practical steps help teams grow with confidence.</li>
    </ul>
    <div class="slide-foot">WWW.RIDGEWAY-CO.COM</div>
  </section>

  <section class="piece slide slide-team col-a row-2">
    <div class="slide-head"><span class="mark"></span><span class="heading">HEADING HERE</span></div>
    <p class="intro">We guide leaders and teams through lasting change.</p>
    <div class="team">
      <div class="member"><div class="portrait" role="img" aria-label="Team member portrait photo"></div><i>Team member1</i>Title<br>Short bio text here.</div>
      <div class="member"><div class="portrait" role="img" aria-label="Team member portrait photo"></div><i>Team member2</i>Title<br>Short bio text here.</div>
      <div class="member"><div class="portrait" role="img" aria-label="Team member portrait photo"></div><i>Team member3</i>Title<br>Short bio text here.</div>
      <div class="member"><div class="portrait" role="img" aria-label="Team member portrait photo"></div><i>Team member4</i>Title<br>Short bio text here.</div>
    </div>
    <div class="slide-foot">WWW.RIDGEWAY-CO.COM</div>
  </section>

  <section class="piece slide slide-list col-b row-2">
    <div class="slide-head"><span class="mark"></span><span class="heading">HEADING HERE</span></div>
    <ul class="bullets">
      <li>Listening comes first in every engagement.</li>
      <li>Behavior insights guide each next step.</li>
      <li>Small habits build durable results over time.</li>
      <li>Coaches partner closely with every client.</li>
      <li>Progress is reviewed and shared openly.</li>
    </ul>
    <div class="slide-foot">WWW.RIDGEWAY-CO.COM</div>
  </section>

  <section class="piece slide slide-feature col-a row-3">
    <div class="slide-head"><span class="mark"></span><span class="heading">HEADING HERE</span></div>
    <p class="lead">Helping people lead with clarity and care.</p>
    <div class="copy">
      <p>Our approach blends coaching with behavioral science to support steady growth.</p>
      <p>Each program is tailored to the goals of your organization.</p>
    </div>
    <div class="photo" role="img" aria-label="Photo of glass office towers against a blue sky"></div>
    <div class="slide-foot">WWW.RIDGEWAY-CO.COM</div>
  </section>

  <section class="piece slide slide-thanks col-b row-3">
    <div class="scenery" role="img" aria-label="Faint mountain range illustration"></div>
    <div class="word">THANKS</div>
    <div class="details">(555) 014-2290<br>dana@ridgeway-co.com<br>www.ridgeway-co.com</div>
    <div class="address">218 Alder Row<br>Suite 12<br>Fairhaven, NC 28100</div>
  </section>

</main>
</body>
</html>
```